Quick Start Android App Design Required!

We're designing an app to revolutionize data collection for outdoor works and road repairs. The app is currently being developed on Android and is due for launch later this year. We've created some functional wireframes that show how the app is to behave. We need you to make them look amazing!

Our intended audience is non-technical, and we'll need the app to be easy to navigate. We need a clean interface that is consistent with the Android interface. We expect you to use common Android design components and we're open to using the new Android Material design language.

We've included a set of wireframes that should show you what we're thinking, there are 12 screens that we need designed. We need your input on colors, fonts, layouts, and borders. If you use images, we'd prefer to see them only on the landing page.

To make things even easier, we have included designs for our website to show you what kind of design we like. Obviously we'd like to keep a consistent theme between the app and the website. We've included a copy of the logo for you to use where necessary too. Take note that we retain copyright to all materials included with this request.
Updates

Project Deadline Extended
Reason: We have decided to extend the deadline. There has been some late interest shown in the project and we'd like to give these designers the opportunity to refine their submissions.

Target Market(s)

Outdoor workers.

Industry/Entity Type

Android

Font styles to use
Serif
Sans Serif

Colors
3176b5

Requirements
Must have
• See the brief, all pages, designed as per brief.
Nice to have
• N/A
Should not have
• Too many images, please keep the design clean and simple.

```html
<!DOCTYPE html>
<html lang="en">
<head>
<meta charset="utf-8">
<title>Job Summary Screens</title>
<link href="https://fonts.googleapis.com/css2?family=Roboto:wght@400;500;700&display=swap" rel="stylesheet">
<style>
  :root {
    --canvas: #d3d3d3;
    --status-bar: #03558f;
    --app-bar: #0468b1;
    --surface: #ffffff;
    --ink: #111111;
    --muted: #a9a9a9;
    --photo-band: #cce0ef;
    --map-tone: #e8e4dc;
    --action-bar: #f4f4f4;
    --action-text: #1a5aa8;
  }
  * { box-sizing: border-box; margin: 0; padding: 0; }
  html, body { width: 1200px; height: 1000px; overflow: hidden; }
  body {
    background: var(--canvas);
    font-family: "Roboto", Arial, sans-serif;
    position: relative;
  }
  .screen {
    position: absolute;
    width: 403px;
    background: var(--surface);
    overflow: hidden;
    box-shadow: 0 2px 4px rgba(0,0,0,0.35);
  }
  .screen--top { left: 133px; top: 144px; height: 720px; }
  .screen--scrolled { left: 660px; top: 148px; height: 716px; }
  .screen-head { position: relative; z-index: 2; }
  .status-bar { height: 26px; background: var(--status-bar); }
  .app-bar {
    height: 63px;
    background: var(--app-bar);
    color: #fff;
    display: flex;
    align-items: center;
    justify-content: space-between;
    padding: 2px 34px 0 31px;
  }
  .app-bar__title { font-size: 22px; font-weight: 500; }
  .app-bar__edit { width: 21px; height: 21px; }
  .el { position: absolute; white-space: nowrap; }
  .job-id { left: 30px; top: 119px; font-size: 26.5px; font-weight: 400; color: var(--ink); }
  .job-date { left: 33px; top: 170px; font-size: 17.8px; color: var(--ink); }
  .job-team { left: 33px; top: 206px; font-size: 17.8px; color: var(--ink); }
  .task { font-size: 17.8px; color: var(--muted); }
  .section-label { font-size: 17.8px; color: var(--muted); }
  .photo-band { position: absolute; left: 0; width: 403px; background: var(--photo-band); overflow: hidden; z-index: 1; }
  .photo-tile { position: absolute; width: 122px; background: var(--surface); border-radius: 2px; }
  .map-area { position: absolute; left: 0; top: 344px; width: 403px; height: 199px; background: linear-gradient(160deg, #ece9e2, var(--map-tone)); }
  .address { left: 31px; top: 559px; font-size: 17.8px; line-height: 21.5px; color: var(--muted); font-style: normal; }
  .action-bar {
    position: absolute; left: 0; bottom: 0; width: 403px; height: 70px;
    background: var(--action-bar);
    display: flex; align-items: center; justify-content: center;
    padding-right: 6px;
    color: var(--action-text); font-size: 17.5px; font-weight: 700; letter-spacing: 0.3px;
  }
</style>
</head>
<body>

<section class="screen screen--top">
  <div class="screen-head">
    <div class="status-bar"></div>
    <header class="app-bar">
      <span class="app-bar__title">Summary</span>
      <svg class="app-bar__edit" viewBox="0 0 24 24"><path fill="#fff" d="M3 17.25V21h3.75L17.81 9.94l-3.75-3.75L3 17.25zM20.71 7.04a1 1 0 0 0 0-1.41l-2.34-2.34a1 1 0 0 0-1.41 0l-1.83 1.83 3.75 3.75 1.83-1.83z"/></svg>
    </header>
  </div>
  <h1 class="el job-id">Job_ID</h1>
  <p class="el job-date">17 August 2015</p>
  <p class="el job-team">Name Of The Team</p>
  <p class="el task" style="left:33px;top:247px">Mowing</p>
  <p class="el task" style="left:203px;top:247px">12&nbsp; Unit</p>
  <p class="el task" style="left:33px;top:279px">Fertilizing</p>
  <p class="el task" style="left:203px;top:279px">39&nbsp; Unit</p>
  <p class="el section-label" style="left:33px;top:356px">9 Photos</p>
  <div class="photo-band" style="top:394px;height:277px">
    <div class="photo-tile" style="left:8px;top:12px;height:122px"></div>
    <div class="photo-tile" style="left:139px;top:12px;height:122px"></div>
    <div class="photo-tile" style="left:270px;top:12px;height:122px"></div>
    <div class="photo-tile" style="left:8px;top:143px;height:122px"></div>
    <div class="photo-tile" style="left:139px;top:143px;height:122px"></div>
    <div class="photo-tile" style="left:270px;top:143px;height:122px"></div>
  </div>
  <p class="el section-label" style="left:33px;top:687px">Locations</p>
</section>

<section class="screen screen--scrolled">
  <div class="screen-head">
    <div class="status-bar"></div>
    <header class="app-bar">
      <span class="app-bar__title">Summary</span>
      <svg class="app-bar__edit" viewBox="0 0 24 24"><path fill="#fff" d="M3 17.25V21h3.75L17.81 9.94l-3.75-3.75L3 17.25zM20.71 7.04a1 1 0 0 0 0-1.41l-2.34-2.34a1 1 0 0 0-1.41 0l-1.83 1.83 3.75 3.75 1.83-1.83z"/></svg>
    </header>
  </div>
  <div class="photo-band" style="top:89px;height:200px">
    <div class="photo-tile" style="left:8px;top:-64px;height:122px"></div>
    <div class="photo-tile" style="left:139px;top:-64px;height:122px"></div>
    <div class="photo-tile" style="left:270px;top:-64px;height:122px"></div>
    <div class="photo-tile" style="left:8px;top:67px;height:122px"></div>
    <div class="photo-tile" style="left:139px;top:67px;height:122px"></div>
    <div class="photo-tile" style="left:270px;top:67px;height:122px"></div>
  </div>
  <p class="el section-label" style="left:32px;top:307px">Locations</p>
  <div class="map-area" role="img" aria-label="Street map showing the job location"></div>
  <address class="el address">42 Fern Lane<br>Brookvale QLD 4210<br>Australia</address>
  <div class="action-bar">SUBMIT</div>
</section>

</body>
</html>
```